Financial firm simple design

Classic business card design for a financial fund. 2 sided card- white on both sides.. One with just the company name centered and the other w the info. info included on that is :

Name
Company position
phone number
fax
email
website

Financial

```html
<!DOCTYPE html>
<html lang="en">
<head>
<meta charset="utf-8">
<title>Halden Investments – Business Card</title>
<link rel="stylesheet" href="https://fonts.googleapis.com/css2?family=Cinzel:wght@400&family=Libre+Baskerville:wght@400&display=swap">
<style>
  :root {
    --backdrop: #ecebe8;
    --card: #ffffff;
    --frame: #0d0d0d;
    --navy: #1f3a6e;
    --ink: #1a1a1a;
    --rule: #6b6b6b;
  }
  * { margin: 0; padding: 0; box-sizing: border-box; }
  html, body { width: 1200px; height: 784px; overflow: hidden; }
  body {
    background: var(--backdrop);
    display: flex;
    align-items: center;
    justify-content: center;
    gap: 48px;
  }
  .card {
    position: relative;
    width: 520px;
    height: 300px;
    background: var(--card);
    box-shadow: 0 2px 10px rgba(0,0,0,.12);
  }
  .card__frame {
    position: absolute;
    inset: 12px;
    border: 9px solid var(--frame);
  }
  .card__content {
    position: absolute;
    inset: 21px;
    display: flex;
    align-items: center;
  }

  /* Contact side */
  .contact { justify-content: flex-start; padding-left: 78px; }
  .identity {
    text-align: right;
    padding-right: 14px;
    font-family: "Libre Baskerville", Georgia, serif;
  }
  .identity__name { color: var(--navy); font-size: 19px; line-height: 1.2; }
  .identity__role { color: var(--ink); font-size: 13px; margin-top: 2px; }
  .divider { width: 1px; height: 66px; background: var(--rule); }
  .details {
    list-style: none;
    padding-left: 12px;
    font-family: "Libre Baskerville", Georgia, serif;
    font-size: 12.5px;
    color: var(--ink);
  }
  .details li { display: flex; align-items: center; gap: 6px; line-height: 17px; }
  .details svg { width: 12px; height: 12px; flex: none; }

  /* Brand side */
  .brand { justify-content: center; }
  .brand__name {
    font-family: "Cinzel", "Times New Roman", serif;
    font-weight: 400;
    font-size: 30px;
    letter-spacing: 1px;
    color: var(--navy);
    text-transform: uppercase;
  }
</style>
</head>
<body>

  <section class="card card--contact" aria-label="Card back with contact details">
    <div class="card__frame"></div>
    <div class="card__content contact">
      <div class="identity">
        <div class="identity__name">Daniel Marsh</div>
        <div class="identity__role">Manager</div>
      </div>
      <div class="divider"></div>
      <ul class="details">
        <li>
          <svg viewBox="0 0 12 12" aria-hidden="true"><path fill="#1a1a1a" d="M2.4 1c.4 0 .7.2.8.5l.7 1.8c.1.3 0 .6-.2.8l-.9.7c.6 1.3 1.6 2.3 2.9 2.9l.7-.9c.2-.2.5-.3.8-.2l1.8.7c.3.1.5.4.5.8V10c0 .6-.4 1-1 1C4.6 11 1 7.4 1 2.9v-.9C1 1.4 1.4 1 2 1z"/></svg>
          07 41802266
        </li>
        <li>
          <svg viewBox="0 0 12 12" aria-hidden="true"><rect x="3" y="1" width="6" height="3" fill="none" stroke="#1a1a1a"/><rect x="1" y="4" width="10" height="5" rx="1" fill="#1a1a1a"/><rect x="3" y="8" width="6" height="3" fill="#fff" stroke="#1a1a1a"/></svg>
          07 41802267
        </li>
        <li>
          <svg viewBox="0 0 12 12" aria-hidden="true"><rect x="1" y="2.5" width="10" height="7" rx="1" fill="#1a1a1a"/><path d="M1.5 3l4.5 3.5L10.5 3" fill="none" stroke="#fff" stroke-width="1"/></svg>
          daniel@haldeninvest.com
        </li>
        <li>
          <svg viewBox="0 0 12 12" aria-hidden="true"><circle cx="6" cy="6" r="5" fill="none" stroke="#1a1a1a"/><ellipse cx="6" cy="6" rx="2.2" ry="5" fill="none" stroke="#1a1a1a"/><path d="M1 6h10M2 3.5h8M2 8.5h8" stroke="#1a1a1a" stroke-width=".8"/></svg>
          www.haldeninvest.com
        </li>
      </ul>
    </div>
  </section>

  <section class="card card--brand" aria-label="Card front with company name">
    <div class="card__frame"></div>
    <div class="card__content brand">
      <div class="brand__name">Halden Investments</div>
    </div>
  </section>

</body>
</html>
```